Website design for a construction company

The logo and the copies of all the 3 pages are attached below. I don't have a preference in colors but I would ideally like to use the colors on my logo, dark teal (secondary) and copper (primary).

Company Name: Corvel Group

Location: London, UK

Business Overview:

Corvel Group is a comprehensive construction company based in London, specializing in a wide range of construction services. We cater to various sectors, providing services including electrical work, painting and decorating, plastering, plumbing, carpentry, kitchen and bathroom installations, loft conversions, and extensions. Our team is known for its skilled craftsmanship, attention to detail, and commitment to quality.

What "CORVEL" stands for:

Our company name, 'CORVEL', is derived from Corvelion, the ancient Greek god of craftsmen, blacksmiths, artisans, sculptors, metals, metallurgy, fire, and volcanoes. Corvelion was renowned in mythology for his incredible skill in crafting and creating, making him the patron of all craftsmen and artisans. His name is synonymous with the mastery of artisanship and the creation of wondrous, enduring works.

In choosing 'CORVEL' as our name, we embody the spirit and skills of Corvelion. It reflects our commitment to craftsmanship, excellence, and durability in the field of construction. Just as Corvelion was known for his meticulous work, precision, and innovative creations, our company strives to uphold these qualities in every project we undertake.

Our name is a constant reminder of our dedication to quality, innovation, and the art of building. It symbolizes our endeavor to achieve the highest standards in construction, much like Corvelion did in his timeless creations. In essence, 'CORVEL' is not just our name; it's a representation of our ethos and the high standards we set for ourselves in the construction industry.

Target Audience:

Our primary audience includes homeowners, real estate developers, and commercial clients in London seeking reliable, high-quality construction services.

Unique Selling Points:

Diverse Range of Services: Offering a one-stop solution for all construction needs.

Certified and Experienced: Professional team with a strong focus on delivering certified and compliant work, particularly in electrical services.

Client-Centric Approach: Emphasizing client satisfaction, we tailor our services to meet the unique needs and visions of our clients.

Quality and Reliability: Commitment to high-quality materials, skilled workmanship, and delivering projects on time and within budget.

Website Requirements:

Clean, professional design reflecting the quality and reliability of our services.

User-friendly navigation to easily access information about our services, portfolio, company background, and contact details.

Portfolio section showcasing our past projects with placeholders for images and descriptions.

Integration of a contact form, map for our location, and links to our social media accounts.

Mobile-responsive design to ensure accessibility across various devices.

Purpose of the Website:
The website aims to:

Establish an online presence and credibility in the construction industry.

Provide an informative resource about our services and past projects to potential clients.

Facilitate easy communication and inquiries through an integrated contact system.

Tone and Style:

Professional, informative, and welcoming. The website should convey trustworthiness and expertise in the construction field.

Target Market(s)

homeowners, real estate developers, and commercial clients

Industry/Entity Type

Construction

Number of Pages Required

3 page

Colors

Designer to choose colors to be used in the design.

```html
<!DOCTYPE html>
<html lang="en">
<head>
<meta charset="utf-8">
<title>Corvel Group — Construction in London</title>
<link href="https://fonts.googleapis.com/css2?family=Oswald:wght@300;400;600&family=Poppins:wght@400;500;600&display=swap" rel="stylesheet">
<style>
:root{
  --copper:#B5863F;
  --teal:#17928A;
  --ink:#1B1B1B;
  --text:#333333;
  --grey-bg:#F4F4F4;
  --footer:#0E0E0E;
  --white:#FFFFFF;
}
*{box-sizing:border-box;margin:0;padding:0}
html,body{width:1200px;height:4032px;overflow:hidden}
body{position:relative;background:var(--white);font-family:'Poppins',sans-serif;color:var(--text)}
.abs{position:absolute}
.heading-cond{font-family:'Oswald',sans-serif;font-weight:300;color:var(--ink);text-align:center}
.heading-cond b{font-weight:600}

/* nav */
.site-nav{position:absolute;left:0;top:0;width:1200px;height:69px;background:var(--white)}
.brand{position:absolute;left:142px;top:14px;display:flex;align-items:center;gap:8px}
.brand-mark{width:34px;height:34px;background:var(--copper)}
.brand-name{font-family:'Poppins',sans-serif;font-weight:500;font-size:28px;letter-spacing:1px;color:var(--ink);line-height:1}
.nav-link{position:absolute;top:25px;font-size:12.5px;font-weight:500;color:var(--ink)}
.nav-link.active{color:var(--teal)}
.nav-cta{position:absolute;left:950px;top:19px;width:110px;height:33px;border-radius:5px;background:var(--copper);color:var(--white);font-size:12.5px;font-weight:500;display:flex;align-items:center;justify-content:center}

/* hero */
.hero{position:absolute;left:0;top:69px;width:1200px;height:474px;background:linear-gradient(90deg,#3f3b37 0%,#6a645d 40%,#b9b6b0 70%,#e8e6e2 100%)}
.hero h1{position:absolute;left:142px;top:146px;font-size:47px;line-height:60px;font-weight:600;color:var(--white)}
.hero p{position:absolute;left:142px;top:286px;width:420px;font-size:14.5px;line-height:26px;color:var(--white)}
.hero .btn{position:absolute;left:142px;top:361px;width:108px;height:29px;border-radius:5px;background:var(--copper);color:var(--white);font-size:12px;font-weight:600;display:flex;align-items:center;justify-content:center}

/* about */
.about-mark{position:absolute;left:142px;top:643px;width:392px;height:357px;background:var(--teal);display:flex;align-items:center;justify-content:center}
.about-mark span{font-size:64px;font-weight:600;color:var(--white);letter-spacing:3px}
.about-copy{position:absolute;left:600px;top:692px;width:420px}
.eyebrow{font-size:12px;color:var(--copper)}
.about-copy h2{font-size:33px;line-height:37px;font-weight:600;color:var(--ink);margin-top:2px}
.about-copy p{font-size:11px;line-height:20px;color:var(--text);margin-top:14px}
.read-more{position:absolute;left:600px;top:905px;width:157px;height:42px;border-radius:21px;background:var(--teal);display:flex;align-items:center;gap:10px;padding-left:4px;color:var(--white);font-size:13px}
.read-more i{width:38px;height:34px;background:var(--copper);border-radius:3px;display:block}

/* why */
.why{position:absolute;left:0;top:1092px;width:1200px;height:565px;background:var(--copper);color:var(--white);text-align:center}
.why h2{position:absolute;left:0;width:1200px;top:76px;font-family:'Oswald',sans-serif;font-weight:400;font-size:42px;color:var(--white)}
.why-item{position:absolute}
.why-item h3{font-family:'Oswald',sans-serif;font-weight:400;font-size:20px;line-height:28px}
.why-item p{font-size:12.5px;line-height:21.5px;margin-top:4px}
.why-center{position:absolute;left:518px;top:326px;width:166px;height:153px;display:flex;align-items:center;justify-content:center;font-size:34px;font-weight:600;letter-spacing:2px;color:var(--white)}

/* services */
.section-title{position:absolute;left:0;width:1200px;font-size:34px}
.section-sub{position:absolute;text-align:center;font-size:12.5px;line-height:22px;color:var(--text)}
.service-photo{position:absolute;left:376px;top:1850px;width:449px;height:313px;border-radius:16px;background:linear-gradient(135deg,#d9d6d2,#8a8680 55%,#2e3a58)}
.service{position:absolute;display:flex;align-items:center;gap:12px;font-size:12.5px;font-weight:600;color:var(--ink);line-height:16px}
.service.left{justify-content:flex-end;text-align:right;width:330px;left:24px}
.service.right{left:849px}
.service-icon{width:46px;height:46px;border-radius:50%;background:var(--white);box-shadow:0 2px 8px rgba(0,0,0,.12);flex:none;display:flex;align-items:center;justify-content:center}
.service-icon i{width:18px;height:18px;border:2px solid var(--copper);border-radius:4px;display:block;border-bottom-color:var(--teal)}

/* testimonials */
.testimonials{position:absolute;left:0;top:2249px;width:1200px;height:532px;background:var(--grey-bg)}
.review{position:absolute;top:2466px;width:448px;height:226px;background:var(--white);border-radius:10px;box-shadow:0 2px 10px rgba(0,0,0,.08);text-align:center}
.review .rule-top{position:absolute;left:63px;top:-4px;width:322px;height:3px;background:var(--copper)}
.review .rule-bottom{position:absolute;left:63px;bottom:-1px;width:322px;height:3px;background:var(--teal)}
.review .quote{position:absolute;left:202px;top:-25px;width:44px;height:44px;border-radius:50%;background:var(--copper);color:var(--white);font-family:Georgia,serif;font-size:34px;line-height:54px;font-weight:700}
.review h4{margin-top:33px;font-size:14px;font-weight:600;color:var(--ink)}
.review .stars{color:#F2B43A;font-size:15px;letter-spacing:6px;margin-top:2px}
.review p{font-size:12.5px;line-height:21.5px;padding:0 18px;margin-top:8px;color:var(--text)}
.arrow{position:absolute;top:2544px;width:70px;height:70px;border-radius:50%;display:flex;align-items:center;justify-content:center}
.arrow.prev{left:54px;border:1.5px solid var(--ink)}
.arrow.next{left:1075px;background:var(--teal)}

/* inquiry */
.inquiry{position:absolute;left:207px;top:2875px;width:787px;height:568px;background:var(--teal);border-radius:16px}
.inquiry h2{position:absolute;left:0;top:40px;width:787px;text-align:center;font-family:'Oswald',sans-serif;font-weight:400;font-size:32px;color:var(--white)}
.field-label{position:absolute;font-size:8.5px;color:var(--white)}
.field{position:absolute;height:46px;border:1.5px solid var(--white);border-radius:3px;color:var(--white);font-size:13px;padding:14px 18px}
.submit{position:absolute;left:322px;top:468px;width:142px;height:41px;background:var(--white);border:1.5px solid var(--copper);color:var(--copper);font-size:13px;font-weight:500;display:flex;align-items:center;justify-content:center}

/* cta */
.cta-btn{position:absolute;left:535px;top:3622px;width:143px;height:40px;background:var(--copper);border-radius:3px;color:var(--white);font-size:13px;font-weight:500;display:flex;align-items:center;justify-content:center}

/* footer */
.site-footer{position:absolute;left:0;top:3748px;width:1200px;height:284px;background:var(--footer);color:var(--white)}
.footer-title{position:absolute;top:61px;font-family:'Oswald',sans-serif;font-weight:400;font-size:16px}
.footer-link{position:absolute;left:142px;font-size:12.5px}
.footer-brand{position:absolute;left:450px;top:126px;width:300px;display:flex;align-items:center;justify-content:center;gap:10px}
.footer-brand .brand-mark{width:48px;height:48px}
.footer-brand .brand-name{color:var(--white);font-size:46px;font-weight:400}
.social{position:absolute;top:222px;width:28px;height:28px;border-radius:50%;border:1.5px solid var(--white)}
.contact-line{position:absolute;left:884px;display:flex;align-items:flex-start;gap:10px;font-size:12.5px;line-height:21px}
</style>
</head>
<body>

<header class="site-nav">
  <div class="brand"><span class="brand-mark"></span><span class="brand-name">CORVEL</span></div>
  <span class="nav-link active" style="left:634px">Home</span>
  <span class="nav-link" style="left:701px">About Us</span>
  <span class="nav-link" style="left:787px">Services</span>
  <span class="nav-link" style="left:870px">Projects</span>
  <span class="nav-cta">Contact Us</span>
</header>

<section class="hero" role="img" aria-label="Two builders in hard hats reviewing plans in front of a house under construction">
  <h1>Building Your<br>Dreams Into Reality</h1>
  <p>Expert Craftsmanship Meets Unmatched Reliability in the Heart of London</p>
  <span class="btn">Learn More</span>
</section>

<section class="about">
  <div class="about-mark"><span>CORVEL</span></div>
  <div class="about-copy">
    <div class="eyebrow">About Us</div>
    <h2>Welcome<br>to Corvel Group</h2>
    <p>Where Construction Meets Excellence. Based in London, we are committed to transforming your spaces into exceptional places. Our team is dedicated to delivering the highest quality in every project, attending to every detail with precision and care.</p>
  </div>
  <div class="read-more"><i></i>Read More</div>
</section>

<section class="why" role="img" aria-label="Copper tinted photo of builders on a construction site">
  <h2>Why Choose Us</h2>
  <div class="why-item" style="left:459px;top:144px;width:282px">
    <h3>Quality Assurance</h3>
    <p>Quality is not just a promise, but a practice. Meticulous attention to detail ensures flawless finishes and durable structures, bringing long-lasting satisfaction to our clients.</p>
  </div>
  <div class="why-item" style="left:148px;top:303px;width:280px">
    <h3>Our Expertise</h3>
    <p>Leveraging over 10 years of experience, Corvel Group stands as a beacon of excellence in the construction industry. We handle each project, big or small, with unmatched professionalism and skill.</p>
  </div>
  <div class="why-center">CORVEL</div>
  <div class="why-item" style="left:773px;top:303px;width:280px">
    <h3>Certified Excellence</h3>
    <p>Your safety and satisfaction are our top priorities. We provide electrical certificates and adhere to the highest industry standards, offering peace of mind in every service.</p>
  </div>
</section>

<section class="services">
  <h2 class="section-title heading-cond" style="top:1732px"><b>Our</b> Services</h2>
  <p class="section-sub" style="left:200px;top:1787px;width:800px">Tailored to Your Needs. Discover how we can bring your vision to life, covering every aspect of construction from the initial design to the final touches.</p>
  <div class="service-photo" role="img" aria-label="Plumber kneeling beside a sink with a red toolbox"></div>

  <div class="service left" style="top:1852px">Electric Work<span class="service-icon"><i></i></span></div>
  <div class="service left" style="top:1938px">Painting &amp; Decorating<span class="service-icon"><i></i></span></div>
  <div class="service left" style="top:2022px">Loft Conversions<span class="service-icon"><i></i></span></div>
  <div class="service left" style="top:2110px">Kitchen &amp;<br>Bathroom Installations<span class="service-icon"><i></i></span></div>

  <div class="service right" style="top:1852px"><span class="service-icon"><i></i></span>Plumbing</div>
  <div class="service right" style="top:1938px"><span class="service-icon"><i></i></span>Carpentry</div>
  <div class="service right" style="top:2022px"><span class="service-icon"><i></i></span>Plastering</div>
  <div class="service right" style="top:2110px"><span class="service-icon"><i></i></span>Extensions</div>
</section>

<section class="testimonials"></section>
<h2 class="section-title heading-cond" style="top:2323px"><b>Hear from</b> Our Satisfied Clients</h2>
<p class="section-sub" style="left:210px;top:2377px;width:780px">Our commitment to excellence has earned us the trust of numerous homeowners and businesses in London. Read their stories and understand the Corvel Group difference.</p>

<article class="review" style="left:142px">
  <span class="rule-top"></span><span class="quote">&ldquo;</span>
  <h4>Daniel Hartley</h4>
  <div class="stars">★★★★★</div>
  <p>"Lorem ipsum dolor sit amet, consectetur adipiscing elit, sed do eiusmod tempor incididunt ut labore et dolore magna aliqua. Ut enim ad minim veniam, quis nostrud exercitation ullamco laboris nisi ut aliquip ex ea commodo consequat."</p>
  <span class="rule-bottom"></span>
</article>
<article class="review" style="left:612px">
  <span class="rule-top"></span><span class="quote">&ldquo;</span>
  <h4>Maya Linden</h4>
  <div class="stars">★★★★★</div>
  <p>"Lorem ipsum dolor sit amet, consectetur adipiscing elit, sed do eiusmod tempor incididunt ut labore et dolore magna aliqua. Ut enim ad minim veniam, quis nostrud exercitation ullamco laboris nisi ut aliquip ex ea commodo consequat."</p>
  <span class="rule-bottom"></span>
</article>
<span class="arrow prev"><svg width="28" height="16" viewBox="0 0 28 16"><path d="M27 8H2M8 2 2 8l6 6" fill="none" stroke="#1B1B1B" stroke-width="2"/></svg></span>
<span class="arrow next"><svg width="28" height="16" viewBox="0 0 28 16"><path d="M1 8h25M20 2l6 6-6 6" fill="none" stroke="#fff" stroke-width="2"/></svg></span>

<section class="inquiry">
  <h2>Quick Inquiry</h2>
  <span class="field-label" style="left:62px;top:109px">First Name*</span>
  <div class="field" style="left:62px;top:125px;width:312px">First Name</div>
  <span class="field-label" style="left:413px;top:109px">Last Name*</span>
  <div class="field" style="left:413px;top:125px;width:311px">Last Name</div>
  <span class="field-label" style="left:62px;top:198px">Email Address*</span>
  <div class="field" style="left:62px;top:214px;width:312px">Email Address</div>
  <span class="field-label" style="left:413px;top:198px">Phone Number*</span>
  <div class="field" style="left:413px;top:214px;width:311px">Phone Number</div>
  <span class="field-label" style="left:62px;top:287px">Email Address*</span>
  <div class="field" style="left:62px;top:303px;width:662px;height:141px">Email Address</div>
  <span class="submit">Submit Now</span>
</section>

<section class="cta">
  <h2 class="section-title heading-cond" style="top:3520px;left:5px"><b>Ready</b> to Start Your Project?</h2>
  <p class="section-sub" style="left:150px;top:3579px;width:910px">Contact us today for a consultation and embark on the journey to turn your construction dreams into a stunning reality.</p>
  <span class="cta-btn">Contact Us</span>
</section>

<footer class="site-footer">
  <h3 class="footer-title" style="left:142px">Quick Links</h3>
  <span class="footer-link" style="top:104px">Home</span>
  <span class="footer-link" style="top:139px">About Us</span>
  <span class="footer-link" style="top:173px">Services</span>
  <span class="footer-link" style="top:208px">Projects</span>
  <span class="footer-link" style="top:243px">Contact Us</span>

  <div class="footer-brand"><span class="brand-mark"></span><span class="brand-name">CORVEL</span></div>
  <span class="social" style="left:534px"></span>
  <span class="social" style="left:568px"></span>
  <span class="social" style="left:603px"></span>
  <span class="social" style="left:638px"></span>

  <h3 class="footer-title" style="left:884px">Contact Details</h3>
  <div class="contact-line" style="top:100px">
    <svg width="14" height="20" viewBox="0 0 14 20"><path d="M7 1a6 6 0 0 0-6 6c0 4.5 6 12 6 12s6-7.5 6-12a6 6 0 0 0-6-6z" fill="#fff"/><circle cx="7" cy="7" r="2.3" fill="#0E0E0E"/></svg>
    <span>123, Building Name,<br>Lorem Street, UK 123456</span>
  </div>
  <div class="contact-line" style="top:180px">
    <svg width="20" height="20" viewBox="0 0 20 20"><path d="M5 2l3 4-2 2c1 2.5 3.5 5 6 6l2-2 4 3-2 3C9 18 2 11 2 4z" fill="none" stroke="#fff" stroke-width="1.6"/></svg>
    <span>123-456-7890</span>
  </div>
  <div class="contact-line" style="top:238px">
    <svg width="22" height="16" viewBox="0 0 22 16"><rect x="1" y="1" width="20" height="14" fill="none" stroke="#fff" stroke-width="1.6"/><path d="M1 1l10 8 10-8" fill="none" stroke="#fff" stroke-width="1.6"/></svg>
    <span>info@corvel.com</span>
  </div>
</footer>

</body>
</html>
```